Kavoni. Sunless Tanning Mousse Label

I'm looking for a label creation for a new brand of sunless tanning solutions. They are in 6.7oz bottles (template attached).

For the front of the bottle (see template) I would like an abstract multi coloured design taking up just over half the top of the bottle (approx 60%) and going around the design (this is similar to the design inspiration attached). I would this design to use the attached colour palette of pinks. It can be swirls, drips, squares, lines, whatever you think will look good.

The logo will then be over top of that abstract design in the upper 1/3, in the colour #3fe0d0

Under the abstract design the following text:

Wild Plume (Larger text)
Coral Drift (2nd heading)
1 Hour Sunless Mousse (Sub text)
The No Orange Guarantee! (Sub text)
Vegan Formula (sub text)

The sub texts for above can be fun, have coloured background, different fonts, whatever looks good and is sill fun.

Towards the bottom of the front of bottle we require the sizing information:

200ml 6.7 Fl Oz

On the left side of the front (so in the template the middle smaller section) I would like the phrase "You ain't gotta get ready if you stay ready" Could you please make this as a separate little quote, with a fun design to it. It's like a little hidden gem on the side of the bottle.

On the back of the bottle for now can you please start towards the top with:

Wild Plume Mousse (larger)
Coral drift (second heading)
Deep Mediterranean Inspired Tan (second heading)
Easy to Apply & Streak Free
Vegan friendly & 100% natural DHA tan actives

Under this I require approx 1.5" of Lorem Ipsum for now which will take the place of directions for using the product.

Under that in small writing can we include "Warning: This product does not contain a sunscreen and will not protect against sunburn. For external use only. If skin irritation occurs, discontinue use. Carry out a patch test 24 hours prior to full body use. Store below 25(degrees sign)C."

At the bottom is the smallest yet still legible writing, can we include the ingredients that are listed below.

Target Market(s)

Females 24-35 who take care of themselves and always want to look good. It's a youthful fun product.

Requirements
Must have
• Bright colours, and just screams FUN and youthful.

Ingredients must be listed on the back. They dont' need to take up more than an inch in height, less if possible.
*******************************************

INGREDIENTS: Water (Aqua), Propylene Glycol, Dihydroxyacetone, Peg-6 Caprylic/Capric Glycerides, Dihydroxypropyl Peg-5 Linoleammonium Chloride, Peg-7 Glyceryl Cocoate, Caramel,
Phenoxyethanol, Caprylyl Glycol, Potassium Sorbate, Hexylene Glycol, Glycerin, Helianthus Annuus (Sunflower) Seed Oil, Beta Vulgaris (Beet) Root Extract, Panthenol, Solanum Lycopersicum
(Tomato) Fruit Extract, Vaccinium Macrocarpon (Cranberry) Fruit Extract, L-ascorbic Acid (Vitamin C), Tocopheryl Acetate (Vitamin E), Theobroma Cacao (Cocoa) Seed Butter, Rosa Canina (Rose Hip)
Fruit Oil, Glycine Soja (Soybean) Oil, Cucumis Sativus (Cucumber) Fruit Extract, Blue 1 (CI 42090), Red 40 (CI 16035), Yellow 6 (CI 15985), Green 5 (CI 61570), Yellow 5 (CI 19140), Red 33 (CI 17200)

*****************************
Nice to have
• Several options to choose from, some can include a gradient into geometric shapes, rather than solid colour. Experiment
Should not have
• Do not want it to look medical.
Want colours to stay in the same pink family for the abstract design - can use white also.

```html
<!DOCTYPE html>
<html lang="en">
<head>
<meta charset="utf-8">
<title>Kavoni – Wild Plume Coral Drift Label</title>
<link rel="stylesheet" href="https://fonts.googleapis.com/css2?family=Amatic+SC:wght@700&family=Nunito:wght@800&family=Quicksand:wght@400;500&family=Raleway:wght@300&display=swap">
<style>
  :root {
    --page: #f4f4f4;
    --label: #ffffff;
    --pink-hot: #ff14cf;
    --pink-soft: #ff6be2;
    --pink-pale: #ffb3f0;
    --plum: #c42bb4;
    --white: #ffffff;
  }
  * { margin: 0; padding: 0; box-sizing: border-box; }
  html, body { width: 874px; height: 1200px; overflow: hidden; background: var(--page); }
  .label {
    position: absolute; left: 54px; top: 0;
    width: 765px; height: 1200px;
    background: var(--label); overflow: hidden;
  }
  .abstract-field { position: absolute; left: 0; top: 0; width: 765px; height: 680px; }
  .brand-name {
    position: absolute; left: 0; width: 765px; top: 185px;
    text-align: center;
    font: 800 70px/1 "Nunito", sans-serif;
    color: var(--white); letter-spacing: 1px;
  }
  .brand-name::after {
    content: ""; display: inline-block; width: 16px; height: 16px;
    border-radius: 50%; background: var(--white); margin-left: 6px;
  }
  .stay-ready {
    position: absolute; left: 14px; top: 735px; width: 210px;
    transform: rotate(-20deg); text-align: center;
    font: 800 19px/1.15 "Nunito", sans-serif; color: var(--white);
  }
  .stay-ready span {
    display: inline-block; background: var(--pink-hot);
    padding: 2px 9px; border-radius: 10px; margin: 1px 0;
  }
  .product-name {
    position: absolute; left: 252px; top: 708px;
    font: 700 104px/1 "Amatic SC", sans-serif;
    color: var(--pink-hot); letter-spacing: 1px;
  }
  .shade-name {
    position: absolute; left: 266px; top: 806px;
    font: 300 52px/1 "Raleway", sans-serif; color: var(--plum);
  }
  .features {
    position: absolute; left: 250px; top: 910px;
    border-left: 6px solid var(--pink-hot); border-radius: 3px;
    padding-left: 9px; list-style: none;
    font: 400 22px/29px "Quicksand", sans-serif; color: var(--plum);
  }
  .net-size {
    position: absolute; left: 370px; top: 1098px;
    font: 400 22px/1 "Quicksand", sans-serif; color: var(--plum);
  }
</style>
</head>
<body>
  <main class="label">
    <svg class="abstract-field" viewBox="0 0 765 680" role="img" aria-label="Abstract pattern of concentric rounded pink and white stripes radiating around the brand name">
      <defs>
        <radialGradient id="stripe-glow" cx="0.48" cy="0.36" r="0.7">
          <stop offset="0" stop-color="#ff2fd4"/>
          <stop offset="0.55" stop-color="#ff6be2"/>
          <stop offset="1" stop-color="#ff22d2"/>
        </radialGradient>
      </defs>
      <path d="M0 0 H765 V510 C700 590 600 668 400 672 C250 674 140 630 80 570 C40 540 15 515 0 497 Z" fill="url(#stripe-glow)"/>
    </svg>

    <div class="brand-name">Kavoni</div>

    <p class="stay-ready">
      <span>You ain't gotta</span><br>
      <span>get ready</span><br>
      <span>if you</span><br>
      <span>stay ready</span>
    </p>

    <h1 class="product-name">WILD PLUME</h1>
    <h2 class="shade-name">Coral Drift</h2>

    <ul class="features">
      <li>1 Hour Sunless Mousse</li>
      <li>The No Orange Guarantee!</li>
      <li>Vegan Formula</li>
    </ul>

    <p class="net-size">200ml 6.7 Fl Oz</p>
  </main>
</body>
</html>
```